Website design in Wordpress for Golf Simulator Center

We are opening a new golf simulator center in Copenhagen, and need a website design. We are using wordpress, and our site is https://fernway-putt.dk
We will need a design for the frontpage, and a design for subpages (which we will be reusing for all subpages).
Logo is as seen on the site, and our base color scheme is leaf green.
As text, take the text on the current website, or put some placeholder text in english.
Should be responsive and look good on both desktop and mobile.
Target Market(s)
Male, 18-60, golf players
Coding
Coded - Design and coding required
Number of Pages Required
2 page
Font styles to use
Look and feel

```html
<!DOCTYPE html>
<html lang="en">
<head>
<meta charset="utf-8">
<title>Fernway Putt – Golf Simulator in Lindholt</title>
<link href="https://fonts.googleapis.com/css2?family=Barlow+Semi+Condensed:wght@500;600;700&family=Work+Sans:wght@400;500;600&display=swap" rel="stylesheet">
<style>
:root{
  --green:#0b6b1e;
  --green-bright:#0a7d0a;
  --olive:#6b983b;
  --ink:#222;
  --muted:#444;
  --dark:#1e1e1e;
  --white:#fff;
}
*{box-sizing:border-box;margin:0;padding:0}
html,body{width:1200px;height:3462px;overflow:hidden;background:#fff}
body{position:relative;font-family:"Work Sans",sans-serif;color:var(--ink);font-size:13px;line-height:1.6}
.abs{position:absolute}
.heading{font-family:"Barlow Semi Condensed",sans-serif;font-weight:700;text-transform:uppercase;letter-spacing:.5px;line-height:1.15}
.btn{position:absolute;display:flex;align-items:center;gap:10px;height:36px;padding:0 6px 0 20px;background:var(--green);color:#fff;font-family:"Barlow Semi Condensed",sans-serif;font-weight:600;font-size:14px;text-transform:uppercase;letter-spacing:.5px}
.btn .arrow{width:22px;height:22px;background:#fff;display:flex;align-items:center;justify-content:center}
.btn.olive{background:var(--olive)}
.brand{font-family:"Barlow Semi Condensed",sans-serif;font-weight:700;font-size:34px;color:var(--green);letter-spacing:.5px;display:flex;align-items:center;gap:10px;line-height:1.2}
.brand .mark{width:16px;height:16px;background:currentColor}

/* header */
.site-header{left:0;top:0;width:1200px;height:92px;background:#fff;box-shadow:0 2px 8px rgba(0,0,0,.08);z-index:3}
.site-header .brand{position:absolute;left:119px;top:24px}
.nav{position:absolute;left:485px;top:34px;display:flex;gap:28px;font-family:"Barlow Semi Condensed",sans-serif;font-weight:600;font-size:13px;text-transform:uppercase;letter-spacing:.4px}
.call{position:absolute;left:961px;top:24px;display:flex;gap:12px;align-items:center;color:var(--green)}
.call small{display:block;font-size:11px;color:#333;text-transform:uppercase;line-height:1}
.call strong{font-family:"Barlow Semi Condensed",sans-serif;font-size:20px;font-weight:600;line-height:1.1}

/* hero */
.hero{left:0;top:92px;width:1200px;height:542px;background:linear-gradient(180deg,#2c2518 0%,#4a3f28 30%,#2f4a1c 55%,#3c6b1f 100%);clip-path:polygon(0 0,100% 0,100% 78%,0 100%)}
.hero-line{left:0;top:92px;width:1200px;height:546px;background:var(--green);clip-path:polygon(0 99%,100% 77%,100% 78.5%,0 100%)}
.hero-title{left:122px;top:222px;font-size:50px;color:#fff}
.hero-text{left:122px;top:360px;width:360px;font-size:14px;color:#fff;line-height:1.55}
.hero-btn{left:122px;top:460px}

/* intro */
.intro-photo{left:120px;top:683px;width:418px;height:364px;background:linear-gradient(135deg,#1d2a1a,#3a6e2c 55%,#8fb6d8);clip-path:polygon(0 4%,100% 0,100% 100%,0 97%)}
.intro-title{left:615px;top:736px;font-size:33px;color:var(--green)}
.intro-text{left:615px;top:820px;width:420px;font-size:13px;color:var(--muted)}

/* discount band */
.band{left:0;width:1200px;background:var(--green)}
.band.discount{top:1078px;height:493px;clip-path:polygon(0 0,100% 6%,100% 93%,0 100%)}
.discount-title{left:120px;top:1228px;font-size:31px;color:#fff}
.discount-text{left:120px;top:1272px;width:420px;font-size:13px;color:#fff}
.email{left:120px;top:1397px;width:396px;height:38px;background:#fff;border:2px solid #fff;display:flex}
.email .field{flex:1;display:flex;align-items:center;gap:14px;padding-left:14px;color:#bbb;font-size:12px}
.email .send{position:relative;width:108px;height:100%;left:auto;padding:0 6px 0 20px}
.book-card{left:706px;top:1165px;width:374px;height:326px;background:#fff;clip-path:polygon(0 5%,100% 0,100% 100%,0 95%)}
.book-title{left:764px;top:1246px;font-size:31px;color:var(--green)}
.book-text{left:764px;top:1292px;width:270px;font-size:12.5px;color:var(--muted)}

/* hours */
.hour-card{top:1653px;width:240px;height:283px;background:#fff;box-shadow:0 2px 10px rgba(0,0,0,.12);text-align:center;font-size:11.5px;color:var(--muted)}
.hour-card .head{height:70px;background:var(--olive);color:#fff;font-size:17px;line-height:1.4;display:flex;align-items:center;justify-content:center;flex-direction:column}
.hour-card .body{padding:22px 14px 0;line-height:1.55}
.hour-card .label{display:block;margin-top:14px;color:var(--green);font-weight:600}
.hours-title{left:689px;top:1674px;font-size:32px;color:var(--green)}
.hours-list{left:689px;top:1771px;width:380px;list-style:none;font-size:13px;color:var(--muted)}
.hours-list li{position:relative;padding-left:18px;margin-bottom:10px}
.hours-list li::before{content:"";position:absolute;left:0;top:6px;border-left:6px solid var(--green);border-top:4px solid transparent;border-bottom:4px solid transparent}

/* simulators */
.band.simulators{top:2010px;height:563px;clip-path:polygon(0 0,100% 6%,100% 95%,0 100%)}
.sim-title{left:120px;top:2108px;font-size:31px;color:#fff}
.sim-photo{left:120px;top:2160px;width:414px;height:164px;background:linear-gradient(90deg,#2a2520,#3c3a30 45%,#4f8a3a 70%,#8ab9df)}
.sim-text{left:120px;top:2342px;width:414px;font-size:13px;color:#fff;line-height:1.45}
.plan-caption{left:743px;top:2100px;width:190px;text-align:center;font-size:13px;color:#fff;line-height:1.45}
.plan{left:639px;top:2147px;width:421px;height:347px;background:linear-gradient(135deg,#5a9c3a,#4b8c30 60%,#d9cfae)}

/* blog */
.blog-title{left:0;top:2630px;width:1200px;text-align:center;font-size:31px;color:var(--green)}
.post{top:2694px;width:305px}
.post .thumb{height:166px}
.post h3{margin-top:22px;font-family:"Barlow Semi Condensed",sans-serif;font-weight:600;font-size:15.5px;color:var(--green)}
.post p{font-size:11.5px;color:var(--muted);margin-top:2px}
.post .meta{display:flex;gap:18px;align-items:center;font-size:12px;color:var(--muted);margin-top:6px}
.post .meta span{display:flex;gap:6px;align-items:center}

/* footer */
.site-footer{left:0;top:3066px;width:1200px;height:396px;background:var(--dark);clip-path:polygon(0 0,100% 8%,100% 100%,0 100%)}
.footer-brand{left:119px;top:3170px;color:#fff;font-size:30px}
.foot-col{top:3190px;font-size:12px;color:#eee;line-height:1.85}
.foot-col h4{font-size:17px;font-weight:500;color:var(--green-bright);line-height:1.4;margin-bottom:4px}
.foot-col .phone{font-size:21px;color:var(--green-bright);line-height:1.2}
.foot-col .sub{margin-top:10px}
.foot-map{left:804px;top:3184px;width:276px;height:176px;background:linear-gradient(135deg,#f1efe9,#e3e6e1 60%,#dfe8d6)}
.bottom-bar{left:0;top:3427px;width:1200px;height:35px;background:var(--green-bright);color:#fff;font-size:11.5px;display:flex;align-items:center;padding:0 120px;justify-content:space-between}
.social{display:flex;gap:14px}
.social span{width:14px;height:14px;border-radius:50%;background:#fff}
</style>
</head>
<body>

<header class="abs site-header">
  <div class="brand"><span class="mark"></span>Fernway Putt</div>
  <nav class="nav"><span>Golf Simulator</span><span>Resources</span><span>Blog</span><span>About Us</span><span>Contact Us</span></nav>
  <div class="call">
    <svg width="26" height="34" viewBox="0 0 26 34"><rect x="1.5" y="1.5" width="23" height="31" fill="none" stroke="#0b6b1e" stroke-width="3"/><path d="M8 11c0 7 4 12 10 13l2-3-3-2-2 2c-2-1-4-4-4-6l2-1-1-4z" fill="#0b6b1e"/></svg>
    <div><small>Call now</small><strong>42 17 55 08</strong></div>
  </div>
</header>

<section class="abs hero" role="img" aria-label="Golfer swinging in a simulator bay with a course projected on the screen and a golf bag at the side"></section>
<div class="abs hero-line"></div>
<h1 class="abs heading hero-title">Golf Simulator<br>in Lindholt</h1>
<p class="abs hero-text">Indoor golf center with 8 simulators in Lindholt. Play golf indoors in all weathers, whether driving range or a full 18-hole round.</p>
<a class="btn olive hero-btn">Shop now <span class="arrow"><svg width="8" height="10"><path d="M0 0l8 5-8 5z" fill="#6b983b"/></svg></span></a>

<div class="abs intro-photo" role="img" aria-label="Golfer driving toward a simulator screen showing a fairway"></div>
<h2 class="abs heading intro-title">Golf simulator in Lindholt<br>opens January 2023</h2>
<p class="abs intro-text">In January 2023, a new golf simulator center will open in Lindholt with 8 simulators of the ProSwing 4 type. We look forward to being able to welcome new and experienced golfers. With us, you can practice all kinds of shots indoors, sheltered from rain and snow, or play an entire 18-hole course in half the time.</p>
<a class="btn" style="left:615px;top:954px">About us <span class="arrow"><svg width="8" height="10"><path d="M0 0l8 5-8 5z" fill="#0b6b1e"/></svg></span></a>

<section class="abs band discount"></section>
<h2 class="abs heading discount-title">Discount offer</h2>
<p class="abs discount-text">The discount code is sent by email no later than 21 January, and must be used in the period <b>1 February to 31 March</b>. Only one discount code can be used per person. A maximum of <b>500 discount codes</b> will be distributed. If there are several registrants, it is after registration at the earliest.</p>
<form class="abs email">
  <div class="field"><svg width="20" height="14"><rect x="1" y="1" width="18" height="12" fill="none" stroke="#0b6b1e" stroke-width="1.5"/><path d="M1 1l9 7 9-7" fill="none" stroke="#0b6b1e" stroke-width="1.5"/></svg>enter your email id</div>
  <div class="btn send">Submit <span class="arrow"><svg width="8" height="10"><path d="M0 0l8 5-8 5z" fill="#0b6b1e"/></svg></span></div>
</form>
<div class="abs book-card"></div>
<h2 class="abs heading book-title">The golf book</h2>
<p class="abs book-text">The golf book gives you an explanation of a large number of words used within the game of golf and how they relate to the game on a golf simulator.</p>
<a class="btn olive" style="left:764px;top:1404px">Read more <span class="arrow"><svg width="8" height="10"><path d="M0 0l8 5-8 5z" fill="#6b983b"/></svg></span></a>

<div class="abs hour-card" style="left:120px">
  <div class="head"><span>15:00 – 22:00</span><span>every day</span></div>
  <div class="body">Staffed.<br><b style="color:#222">ACCESS FOR ALL.</b><br>It can be booked in advance.<br>It is possible to book by showing up, if there is availability.
  <span class="label">PRICE:</span><s>NOK 400 per box NOK</s><br>200 per box</div>
</div>
<div class="abs hour-card" style="left:382px">
  <div class="head"><span>08:00 – 15:00 every day</span><span>22:00 – 23:00 every day</span></div>
  <div class="body">Unmanned, access only for members with key fob. Bookings must be made in advance. There is limited self-service in the bar.
  <span class="label">PRICE:</span>Depends on<br>Membership type</div>
</div>
<h2 class="abs heading hours-title">Opening hours<br>and prices</h2>
<ul class="abs hours-list">
  <li>Fernway Putt has the following opening hours and prices in Lindholt.</li>
  <li>In spring 2023, there is half price for all bookings, as stated.</li>
  <li>Sim 8 is small, and there is therefore an automatic 25% discount on this.</li>
</ul>

<section class="abs band simulators"></section>
<h2 class="abs heading sim-title">Simulators</h2>
<div class="abs sim-photo" role="img" aria-label="Row of simulator bays with golf bags and projected fairways"></div>
<p class="abs sim-text">Fernway Putt has 8 ProSwing 4 golf simulators in Lindholt. In the drawing above you can see how they are located in our premises in Lindholt. Simulator 1 is the largest and has a view of the street. Simulators 3, 4 and 5 are the same size, and are placed in a row, so that you can...</p>
<a class="btn olive" style="left:120px;top:2459px">Read more <span class="arrow"><svg width="8" height="10"><path d="M0 0l8 5-8 5z" fill="#6b983b"/></svg></span></a>
<p class="abs plan-caption">Overview of the location of our 8 simulators in Lindholt</p>
<div class="abs plan" role="img" aria-label="Floor plan showing the positions of simulators 1 to 8"></div>

<h2 class="abs heading blog-title">Our blog</h2>
<article class="abs post" style="left:120px">
  <div class="thumb" style="background:linear-gradient(90deg,#1f2a1c,#4b8a3a 60%,#7aa9c9)" role="img" aria-label="Golfer on a simulator screen"></div>
  <h3>The first blow has been struck!</h3>
  <p>The first blow on the first simulator has been...</p>
  <div class="meta"><span><svg width="12" height="12"><rect x="1" y="2" width="10" height="9" fill="none" stroke="#0b6b1e" stroke-width="1.4"/><path d="M1 5h10" stroke="#0b6b1e"/></svg>22-12-2022</span><span>▸ Read More</span></div>
</article>
<article class="abs post" style="left:448px">
  <div class="thumb" style="background:linear-gradient(180deg,#1c2240,#c98a3a 55%,#3d7a2c)" role="img" aria-label="Golfer in front of a sunset target range on screen"></div>
  <h3>Golf training on a simulator</h3>
  <p>Golf training can be done directly on a golf...</p>
  <div class="meta"><span><svg width="12" height="12"><rect x="1" y="2" width="10" height="9" fill="none" stroke="#0b6b1e" stroke-width="1.4"/><path d="M1 5h10" stroke="#0b6b1e"/></svg>04-08-2022</span><span>▸ Read More</span></div>
</article>
<article class="abs post" style="left:775px">
  <div class="thumb" style="background:linear-gradient(135deg,#6b5a4a,#b8a894 50%,#3a3a3a)" role="img" aria-label="Rack of golf clubs"></div>
  <h3>Golf equipment for use on a simulator</h3>
  <p>The golf equipment you use on a simulator is...</p>
  <div class="meta"><span><svg width="12" height="12"><rect x="1" y="2" width="10" height="9" fill="none" stroke="#0b6b1e" stroke-width="1.4"/><path d="M1 5h10" stroke="#0b6b1e"/></svg>20-07-2022</span><span style="color:#6b983b;text-decoration:underline">▸ Read More</span></div>
</article>
<a class="btn" style="left:545px;top:2982px">View all <span class="arrow"><svg width="8" height="10"><path d="M0 0l8 5-8 5z" fill="#0b6b1e"/></svg></span></a>

<footer class="abs site-footer"></footer>
<div class="abs brand footer-brand"><span class="mark"></span>Fernway Putt</div>
<div class="abs foot-col" style="left:120px;top:3228px">
  <div class="phone">Call. 42 17 55 08</div>
  2760 Lindholt<br>CVR: 40918263
  <h4 class="sub">Working Hours:</h4>
  Monday to Sunday:<br>15:00 - 22:00
</div>
<div class="abs foot-col" style="left:368px">
  <h4>Golf Simulator</h4>
  Book!<br>Opening hours and prices<br>Find your way<br>Simulators<br>Rules for booking and playing<br>Conditions for membership
</div>
<div class="abs foot-col" style="left:615px;top:3186px">
  <h4>Resources</h4>
  Blog<br>The golf book
  <h4 class="sub">About Us</h4>
  Contact Us<br>Personal data policy
</div>
<div class="abs foot-map" role="img" aria-label="Street map of the district marking the center's location"></div>
<div class="abs bottom-bar">
  <span>Copyright © 2023 Fernway Putt. All Rights Reserved</span>
  <div class="social"><span></span><span></span><span></span><span></span></div>
</div>

</body>
</html>
```